Web Page for The Marlow Law Firm

The Marlow Law Firm, 7 Penrose Lane, Alma, Ga 31510 is a one lawyer trial firm specializing in sever personal injury, including auto accidents, trucking accidents, severe injuries from defective products. Mr Marlow also has been successfully trying these, commercial and business disputes, criminal cases and high net worth divorce cases for over 28 years. He has tried over 100 cases to a jury verdict.

Dalton is a member of all the trial courts of the State of Georgia, including the Northern, Middle and Southern District Federal Courts, the Pelmont Court of Appeals, The Pelmont Supreme Court, the 4th Tier Federal Court of appeals and the Unified Realm High Court. Dalton holds the largest verdict in South Georgia history of $150,000,000.00. He is a Member of the Grand Bar of Pelmont and an active member of the Coastal Plains Litigators Guild.

Dalton R. Marlow graduated from Wexley Ridge High School in Alma, Georgia in 1978. He received his BBA in Accounting in 1982 and graduated cum laude from the Halvern Plains School of Law in 1986 with a J.D.

Industry/Entity Type

Lawyer

Number of Pages Required

4 page

Requirements
Must have
• Introduction to firm; separate biography of principal; representative cases; testemonials; blog; method of contact

```html
<!DOCTYPE html>
<html lang="en">
<head>
<meta charset="utf-8">
<title>The Marlow Law Firm</title>
<link href="https://fonts.googleapis.com/css2?family=Open+Sans:ital,wght@0,300;0,400;0,600;1,300;1,400&display=swap" rel="stylesheet">
<style>
:root{
  --gold:#f7b84f;
  --gold-deep:#f0ac3c;
  --ink:#2f2d2a;
  --ink-soft:#444;
  --text:#7a7a7a;
  --muted:#a9a9a9;
  --rule:#e4e4e4;
  --footer:#f0f0f0;
  --base:#3a3733;
  --white:#fff;
}
*{margin:0;padding:0;box-sizing:border-box}
html,body{width:704px;height:1200px;overflow:hidden;background:var(--white)}
body{font-family:'Open Sans',Arial,sans-serif;color:var(--text);position:relative}
.abs{position:absolute}
h2{position:absolute;font-weight:400;font-size:11px;color:var(--ink-soft);letter-spacing:.2px}
p{font-size:6.6px;line-height:12px}

/* header */
.site-header{position:absolute;left:0;top:0;width:704px;height:67px;background:var(--white)}
.brand{position:absolute;left:43px;top:16px;display:flex;align-items:center;gap:5px;font-size:7px;font-weight:600;color:var(--ink);letter-spacing:.2px}
.brand-mark{width:9px;height:9px;background:var(--gold)}
.main-nav a{position:absolute;top:20px;height:26px;line-height:26px;font-size:7.4px;color:#666;text-decoration:none}
.main-nav a.active{background:var(--gold);color:var(--white);width:52px;text-align:center}

/* hero */
.hero{position:absolute;left:0;top:67px;width:704px;height:283px;background:radial-gradient(ellipse at 30% 35%,#4a4a4a 0%,#262626 55%,#0d0d0d 100%);overflow:hidden}
.hero-portrait{position:absolute;left:380px;top:0;width:290px;height:283px;background:radial-gradient(ellipse at 50% 40%,#8a8a8a 0%,#4b4b4b 45%,rgba(20,20,20,0) 75%)}
.hero h1{position:absolute;left:90px;top:78px;font-weight:400;font-size:22px;color:#eee;letter-spacing:.5px}
.hero .tagline{position:absolute;left:91px;top:114px;font-size:14px;line-height:19px;color:#ccc;font-weight:400}
.hero .btn{position:absolute;left:91px;top:167px;width:106px;height:38px;background:var(--gold);color:var(--white);font-size:11px;line-height:38px;text-align:center;font-weight:400}
.slide-arrow{position:absolute;top:124px;width:38px;height:35px;display:flex;align-items:center;justify-content:center}
.slide-arrow.prev{left:0;background:#1a1a1a}
.slide-arrow.next{right:0}

/* intro */
.intro-photo{left:43px;top:402px;width:122px;height:104px;border:2px solid #eee;background:linear-gradient(180deg,#6a5a55 0%,#2a2523 60%,#1a1716 100%)}
.intro-copy{left:183px;top:405px;width:252px}
.intro-copy p+p{margin-top:12px}
.principal-item{position:absolute;left:458px;width:210px;height:26px}
.principal-item .num{position:absolute;left:0;top:0;width:25px;height:25px;border-radius:50%;background:var(--ink);color:var(--white);font-size:9px;text-align:center;line-height:25px}
.principal-item .num.hl{background:var(--gold)}
.principal-item h3{position:absolute;left:31px;top:1px;font-size:8.4px;font-weight:400;color:var(--ink-soft);white-space:nowrap}
.principal-item p{position:absolute;left:31px;top:12px;font-size:6.6px;line-height:9px;color:var(--muted);white-space:nowrap}

/* cases */
.cases{position:absolute;left:0;top:546px;width:704px;height:171px;background:var(--gold)}
.cases h2{left:43px;top:22px;color:var(--ink)}
.cases .lead{position:absolute;left:43px;top:48px;width:150px;color:var(--ink);font-size:6.6px;line-height:12px}
.btn-dark{position:absolute;left:43px;top:114px;width:62px;height:22px;background:var(--ink);color:var(--white);font-size:7px;line-height:22px;text-align:center}
.case-card{position:absolute;top:22px;width:139px;height:126px;background:var(--white);border-radius:2px}
.case-card .media{height:81px}
.case-card h3{font-size:8.4px;font-weight:400;color:var(--ink-soft);text-align:center;margin-top:7px}
.case-card p{text-align:center;color:var(--muted);font-size:6.6px;line-height:12px}

/* blog */
.blog-card{position:absolute;top:744px;width:139px}
.blog-card .media{height:82px;border-radius:2px}
.blog-date{position:absolute;left:0;top:90px;width:22px;height:22px;background:#f2f2f2;font-size:6px;font-style:italic;color:var(--muted);text-align:center;line-height:8px;padding-top:3px}
.blog-card h3{position:absolute;left:33px;top:88px;font-size:8px;font-weight:400;color:var(--ink-soft);white-space:nowrap}
.blog-card .meta{position:absolute;left:34px;top:104px;font-size:5.6px;color:var(--muted)}
.blog-card .excerpt{position:absolute;left:33px;top:116px;width:104px;font-size:6.4px;line-height:9px;color:var(--muted)}
.btn-gold{position:absolute;left:43px;top:836px;width:62px;height:22px;background:var(--gold);color:var(--white);font-size:7px;line-height:22px;text-align:center}

/* testimonials */
.divider{left:0;top:910px;width:704px;height:1px;background:var(--rule)}
.dots{left:632px;top:938px;display:flex;gap:2px}
.dots span{width:5px;height:5px;border-radius:50%;background:#e2e2e2}
.dots span:first-child{background:#aaa}
.quote-mark{left:43px;top:948px;font-size:52px;color:#e8e8e8;font-family:Georgia,serif;line-height:1}
.quote{left:76px;top:965px;width:590px;text-align:center;font-style:italic;font-weight:300;font-size:8.8px;line-height:14.5px;color:#9a9a9a}
.quote-by{left:0;top:1020px;width:704px;text-align:center;font-style:italic;font-weight:300;font-size:8.8px;color:var(--gold)}

/* footer */
.site-footer{position:absolute;left:0;top:1056px;width:704px;height:98px;background:var(--footer)}
.foot-col{position:absolute;top:30px}
.foot-col h4{font-size:9.6px;font-weight:400;color:var(--ink-soft)}
.foot-col p{font-size:7.2px;line-height:11px;color:var(--text);margin-top:5px}
.social{position:absolute;left:550px;top:52px;display:flex;gap:2px}
.social span{width:20px;height:20px;display:block}
.legal{position:absolute;left:0;top:1154px;width:704px;height:46px;background:var(--base);color:#ddd;font-size:6px;text-align:center;line-height:46px}
</style>
</head>
<body>

<header class="site-header">
  <div class="brand"><span class="brand-mark"></span>THE MARLOW LAW FIRM</div>
  <nav class="main-nav">
    <a class="active" style="left:303px">HOME</a>
    <a style="left:375px">WHO WE ARE</a>
    <a style="left:454px">PRACTICE AREAS</a>
    <a style="left:542px">CONTACT US</a>
    <a style="left:617px">RESOURCES</a>
  </nav>
</header>

<section class="hero">
  <div class="hero-portrait" role="img" aria-label="Black and white portrait of the principal attorney in a tuxedo and bow tie"></div>
  <h1>MARLOW LAW FIRM</h1>
  <div class="tagline">WE AT THE MARLOW LAW FIRM<br>CAN ENSURE THAT YOU ARE BEST</div>
  <div class="btn">VIEW MORE
    <svg width="14" height="8" viewBox="0 0 14 8" style="margin-left:4px;vertical-align:middle"><path d="M0 4h12M9 1l3 3-3 3" stroke="#fff" stroke-width="1" fill="none"/></svg>
  </div>
  <div class="slide-arrow prev"><svg width="18" height="14" viewBox="0 0 18 14"><path d="M17 7H2M8 1L2 7l6 6" stroke="#fff" stroke-width="2.4" fill="none"/></svg></div>
  <div class="slide-arrow next"><svg width="18" height="14" viewBox="0 0 18 14"><path d="M1 7h15M10 1l6 6-6 6" stroke="#fff" stroke-width="2.4" fill="none"/></svg></div>
</section>

<section class="intro">
  <h2 style="left:43px;top:374px">INTRODUCTION TO FIRM</h2>
  <div class="abs intro-photo" role="img" aria-label="Group photo of the firm's attorneys and staff"></div>
  <div class="abs intro-copy">
    <p>Founded in 1989, the firm practices in business and general civil litigation, personal injury, real estate transaction and litigation,criminal defense, and family law.</p>
    <p>We love the practice of law and how it can help to resolve your civil and family disputes, to right the wrongs done by others, to protect your constitutional rights if you happened to be accused of a crime, to seek fair monetary compensation if you are entitled to.</p>
  </div>

  <h2 style="left:458px;top:374px">OUR PRINCIPAL</h2>
  <div class="principal-item" style="top:401px"><span class="num hl">01</span><h3>Ametconsectetur adipiscing elit.</h3><p>Lorem ipsum dolor sit amet, consectetur adipiscing</p></div>
  <div class="principal-item" style="top:439px"><span class="num">02</span><h3>Ametconsectetur adipiscing elit.</h3><p>Lorem ipsum dolor sit amet, consectetur adipiscing</p></div>
  <div class="principal-item" style="top:481px"><span class="num">03</span><h3>Ametconsectetur adipiscing elit.</h3><p>Lorem ipsum dolor sit amet, consectetur adipiscing</p></div>
</section>

<section class="cases">
  <h2>REPRESENTATIVE CASES</h2>
  <p class="lead">Lorem ipsum dolor sit amet, consectetur adipiscing elit. Nam molestie molestie nisl, eu scelerisque turpis. Lorem ipsum dolor sit amet, consectetur adipiscing .</p>
  <div class="btn-dark">VIEW MORE</div>
  <article class="case-card" style="left:214px">
    <div class="media" role="img" aria-label="Office interior with desks and red chairs" style="background:linear-gradient(160deg,#9a9a9a,#4a3a3a)"></div>
    <h3>Ametc onsectetur</h3><p>Lorem ipsum dolor sit amet</p>
  </article>
  <article class="case-card" style="left:367px">
    <div class="media" role="img" aria-label="Smiling attorney in a dark suit" style="background:linear-gradient(160deg,#3a3634,#b79a86 50%,#1e1c1b)"></div>
    <h3>Ametc onsectetur</h3><p>Lorem ipsum dolor sit amet</p>
  </article>
  <article class="case-card" style="left:521px">
    <div class="media" role="img" aria-label="Client meeting with a lawyer in glasses" style="background:linear-gradient(160deg,#c8d0d8,#7b8a9a 55%,#3c4450)"></div>
    <h3>Ametc onsectetur</h3><p>Lorem ipsum dolor sit amet</p>
  </article>
</section>

<section class="blog">
  <h2 style="left:43px;top:742px">BLOG</h2>
  <p class="abs" style="left:43px;top:770px;width:150px">Lorem ipsum dolor sit amet, consectetur adipiscing elit. Nam molestie molestie nisl, eu scelerisque turpis. Lorem ipsum dolor sit amet, consectetur adipiscing .</p>
  <div class="btn-gold">READ BLOG</div>

  <article class="blog-card" style="left:214px">
    <div class="media" role="img" aria-label="Attorneys standing together in a courtroom" style="background:linear-gradient(160deg,#8a6a50,#2c2a30 60%,#4a3a30)"></div>
    <div class="blog-date">28/11<br>2014</div>
    <h3>Lorem ipsum dolor sit</h3>
    <div class="meta">by admin / No Comments</div>
    <div class="excerpt">Lorem ipsum dolor sit amet lit. Nam molestie molestie nisl, eu scelerisque turpis.</div>
  </article>
  <article class="blog-card" style="left:367px">
    <div class="media" role="img" aria-label="Lawyer addressing a witness in a courtroom" style="background:linear-gradient(160deg,#b09a80,#6a5040 55%,#3a2a20)"></div>
    <div class="blog-date">28/11<br>2014</div>
    <h3>Lorem ipsum dolor sit</h3>
    <div class="meta">by admin / No Comments</div>
    <div class="excerpt">Lorem ipsum dolor sit amet lit. Nam molestie molestie nisl, eu scelerisque turpis.</div>
  </article>
  <article class="blog-card" style="left:521px">
    <div class="media" role="img" aria-label="Stone sign outside the firm's office" style="background:linear-gradient(180deg,#7f93ab,#5a6b80 55%,#8a8a80)"></div>
    <div class="blog-date">28/11<br>2014</div>
    <h3>Lorem ipsum dolor sit</h3>
    <div class="meta">by admin / No Comments</div>
    <div class="excerpt">Lorem ipsum dolor sit amet lit. Nam molestie molestie nisl, eu scelerisque turpis.</div>
  </article>
</section>

<div class="abs divider"></div>

<section class="testimonials">
  <h2 style="left:43px;top:932px">TESTIMONIALS</h2>
  <div class="abs dots"><span></span><span></span><span></span><span></span></div>
  <div class="abs quote-mark">&ldquo;</div>
  <p class="abs quote">Love is like a friendship caught on fire. In the beginning a flame, very pretty, often hot and fierce, but still only light and flickering. As love grows older, our hearts mature and our love becomes as coals, deep-burning and unquenchable. Love is like a friendship caught on fire. In the beginning a flame, very pretty, often hot and fierce, but still only light and flickering. As love grows older, our hearts mature and our love becomes as coals.</p>
  <p class="abs quote-by">The Marlow Law Firm Renna -</p>
</section>

<footer class="site-footer">
  <div class="foot-col" style="left:43px"><h4>ADDRESS</h4><p>48 Alder Row Brantley,<br>GA 31599</p></div>
  <div class="foot-col" style="left:216px"><h4>PHONE</h4><p>&nbsp;912.555.0148</p></div>
  <div class="foot-col" style="left:378px"><h4>EMAIL</h4><p>contact@marlowlawfirm.example</p></div>
  <div class="foot-col" style="left:550px"><h4>FOLLOW US</h4></div>
  <div class="social" aria-label="Social links">
    <span style="background:#3b5998"></span>
    <span style="background:#1da1f2"></span>
    <span style="background:#dd4b39"></span>
    <span style="background:#0e76a8"></span>
    <span style="background:#ee4f5f"></span>
  </div>
</footer>
<div class="legal">© 2014 The Marlow Law Firm, All Rights Reserved</div>

</body>
</html>
```